Harbor Crest Data Systems Needs a Website Desing

We need a website design for a new company based in Kuwait called Harbor Crest Data Systems (HCDS). We provide Software as a Service (SaaS) solutions for small and medium business companies. We will develop the required E-systems like HR,Payroll,Accounting Systems for those customers who wants to focus on their business instead of wasting time to automate it. HCDS need a web site that represent this activity and showing our cloud products and allow out customers to easily identify their needs. as a normal web site basic things need to be included like :
about HCDS
Solutions
PressRoom
Contact us
please i need something similar to trelvoxa.com or qup.com or www.dro7lak.com with blue and black theme .. please check the Company's logo
Updates
hi all ,,,
the project is only design without any codes
Reason: The project is focus on design only ,, i will be really appreciated to have more designs

```html
<!DOCTYPE html>
<html lang="en">
<head>
<meta charset="utf-8">
<title>HCDS — Solution</title>
<link href="https://fonts.googleapis.com/css2?family=Questrial&family=Arimo:wght@400;700&display=swap" rel="stylesheet">
<style>
  :root {
    --brand-blue: #2d8fdb;
    --link-blue: #1e7fd0;
    --ink-dark: #232323;
    --ink-black: #111111;
    --text-grey: #5a5a5a;
    --heading-grey: #555555;
    --line-grey: #d6d6d6;
    --white: #ffffff;
    --chart-deep: #1d4f9a;
    --chart-light: #9fc4ec;
  }
  * { box-sizing: border-box; margin: 0; padding: 0; }
  html, body { width: 1200px; height: 1200px; overflow: hidden; background: var(--white); }
  body { position: relative; font-family: "Arimo", Arial, sans-serif; color: var(--text-grey); }

  .brand { position: absolute; left: 130px; top: 90px; display: flex; align-items: center; gap: 10px; }
  .brand-dot { width: 50px; height: 50px; border-radius: 50%; background: var(--brand-blue); }
  .brand-name { font-family: "Arimo", Arial, sans-serif; font-weight: 700; font-size: 46px; color: var(--ink-dark); letter-spacing: 1px; }

  .search { position: absolute; left: 867px; top: 99px; width: 204px; height: 28px; border: 1px solid #dfe7ee; border-radius: 14px; background: #fbfdff; }
  .search-placeholder { position: absolute; left: 14px; top: 7px; font-size: 12px; color: #c9d3dc; }
  .search-icon { position: absolute; right: 8px; top: 3px; }

  .main-nav { position: absolute; left: 0; top: 156px; width: 1200px; height: 53px; background: var(--brand-blue); }
  .main-nav a { position: absolute; top: 19px; font-weight: 700; font-size: 15px; color: var(--white); text-decoration: none; }
  .main-nav a.current { color: var(--ink-black); }
  .sub-band { position: absolute; left: 0; top: 209px; width: 1200px; height: 35px; background: var(--ink-dark); border-bottom: 2px solid var(--brand-blue); }

  .news-card { position: absolute; left: 123px; width: 314px; height: 131px; border: 1px solid var(--line-grey); background: var(--white); font-family: "Questrial", sans-serif; }
  .news-card .visual { position: absolute; left: 6px; top: 8px; width: 100px; height: 115px; border-radius: 4px; }
  .visual.chart { background: linear-gradient(160deg, var(--chart-light), var(--chart-deep) 70%, #c9ccd2); }
  .visual.puzzle { background: radial-gradient(circle at 55% 50%, #4c8fd3 0 18%, #e6e8ec 40%, #b9bcc2 100%); }
  .news-card .title { position: absolute; left: 115px; top: 14px; font-size: 15px; color: var(--ink-black); }
  .news-card .detail { position: absolute; left: 115px; top: 42px; font-size: 11.5px; line-height: 14px; color: var(--ink-black); width: 190px; }
  .news-card .more { position: absolute; left: 115px; top: 88px; font-size: 15px; color: var(--link-blue); }

  .copy { position: absolute; left: 453px; width: 612px; }
  .copy h2 { font-size: 13.5px; font-weight: 700; color: var(--heading-grey); letter-spacing: 0.3px; }
  .copy p, .media-text { font-size: 12.5px; line-height: 18px; color: var(--text-grey); }
  .copy p a, .media-text a { color: var(--link-blue); text-decoration: none; }

  .media-visual { position: absolute; left: 451px; top: 670px; width: 269px; height: 138px; background: linear-gradient(120deg, #0d4f9c, #2a86d6 55%, #0f5aa8); }
  .media-text { position: absolute; left: 737px; top: 667px; width: 334px; }

  .newsletter { position: absolute; left: 123px; top: 849px; width: 314px; height: 141px; border-radius: 9px; background: var(--brand-blue); }
  .newsletter h3 { position: absolute; left: 25px; top: 20px; font-size: 15px; font-weight: 700; color: var(--white); }
  .newsletter .email { position: absolute; left: 18px; top: 54px; width: 206px; height: 30px; background: var(--white); border-radius: 3px 0 0 3px; font-size: 12px; color: #c9d0d6; padding: 9px 8px; }
  .newsletter .go { position: absolute; left: 224px; top: 54px; width: 52px; height: 30px; background: var(--ink-dark); border-radius: 0 8px 8px 0; color: var(--white); font-size: 10px; font-weight: 700; text-align: center; line-height: 30px; }
  .newsletter .note { position: absolute; left: 26px; top: 96px; font-size: 11px; font-weight: 700; color: var(--white); }

  .partners { position: absolute; left: 123px; top: 1010px; width: 948px; height: 79px; border: 1px solid var(--line-grey); }
  .badge { position: absolute; top: 9px; height: 60px; }
  .badge.sky { background: linear-gradient(135deg, #27a8e0, #1479c2); }
  .badge.slate { background: #6b7fc3; }
  .badge.pale { background: #eeeeee; top: 20px; height: 38px; }
  .badge.night { background: var(--ink-black); }

  .site-footer { position: absolute; left: 0; top: 1104px; width: 1200px; height: 37px; background: var(--ink-dark); font-size: 12px; color: #e3e3e3; }
  .site-footer span { position: absolute; top: 12px; }
  .social-dot { position: absolute; top: 10px; width: 17px; height: 17px; border-radius: 50%; background: #4a6a8a; }
  .footer-base { position: absolute; left: 0; top: 1141px; width: 1200px; height: 59px; background: var(--brand-blue); border-top: 1px solid #9cc8ee; }
</style>
</head>
<body>
  <header>
    <div class="brand"><span class="brand-dot"></span><span class="brand-name">HCDS</span></div>
    <div class="search">
      <span class="search-placeholder">Search</span>
      <svg class="search-icon" width="22" height="22" viewBox="0 0 22 22"><circle cx="9" cy="9" r="6.5" fill="none" stroke="#9fb6c9" stroke-width="2"/><line x1="14" y1="14" x2="20" y2="20" stroke="#9fb6c9" stroke-width="3" stroke-linecap="round"/></svg>
    </div>
  </header>

  <nav class="main-nav">
    <a style="left:133px">HOME</a>
    <a class="current" style="left:237px">SOLUTION</a>
    <a style="left:368px">SERVICES</a>
    <a style="left:499px">SUPPORT</a>
    <a style="left:629px">HOW TO BUY</a>
    <a style="left:771px">COMMUNITIES</a>
  </nav>
  <div class="sub-band"></div>

  <article class="news-card" style="top:278px">
    <div class="visual chart" role="img" aria-label="3D blue bar chart graphic"></div>
    <div class="title">QUP REPORT FIRST DATA 2013</div>
    <div class="detail">Financial Result</div>
    <div class="more">Learn More</div>
  </article>
  <article class="news-card" style="top:428px">
    <div class="visual puzzle" role="img" aria-label="Jigsaw puzzle pieces with one blue piece"></div>
    <div class="title" style="left:113px">12 Feb 2013,</div>
    <div class="detail" style="top:40px">Proactive Storage Management with QUP Storage Analytics</div>
    <div class="more">Learn More</div>
  </article>
  <article class="news-card" style="top:577px">
    <div class="visual chart" role="img" aria-label="3D blue bar chart graphic"></div>
    <div class="title">QUP REPORT FIRST DATA 2013</div>
    <div class="detail">Financial Result</div>
    <div class="more">Learn More</div>
  </article>

  <section class="copy" style="top:287px">
    <h2>SOLUTION PROVIDE BY COMPANY</h2>
  </section>
  <section class="copy" style="top:319px">
    <p>We need a website design for a new company based in Kuwait called <a>Harbor Crest Data Systems (HCDS)</a>. We provide Software as a Service (SaaS) solutions for small and medium business companies. We will develop the required E-systems like HR,Payroll,Accounting Systems for those customers who wants to focus on their business instead of wasting time to automate it.</p>
  </section>
  <section class="copy" style="top:427px">
    <p>We need a website design for a new company based in Kuwait called <a>Harbor Crest Data Systems (HCDS)</a>. We provide Software as a Service (SaaS) solutions for small and medium business companies. We will develop the required E-systems like HR,Payroll,Accounting Systems for those customers who wants to focus on their business instead of wasting time to automate it.</p>
  </section>
  <section class="copy" style="top:541px">
    <h2>SOLUTION</h2>
  </section>
  <section class="copy" style="top:573px">
    <p>We need a website design for a new company based in Kuwait called <a>Harbor Crest Data Systems (HCDS)</a>. We provide Software as a Service (SaaS) solutions for small and medium business companies. We will develop the required E-systems like HR,Payroll,Accounting Systems for those customers who wants to focus on their business instead of wasting time to automate it.</p>
  </section>

  <div class="media-visual" role="img" aria-label="Software box turning into an HTML box, on a blue background"></div>
  <p class="media-text">We need a website design for a new company based in Kuwait called <a>Harbor Crest Data Systems (HCDS)</a>. We provide Software as a Service (SaaS) solutions for small and medium business companies. We will develop the required E-systems like HR,Payroll,Accounting Systems for those customers who wants to focus on their business instead of wasting time to automate it.</p>

  <section class="copy" style="top:847px">
    <p>We need a website design for a new company based in Kuwait called <a>Harbor Crest Data Systems (HCDS)</a>. We provide Software as a Service (SaaS) solutions for small and medium business companies. We will develop the required E-systems like HR,Payroll,Accounting Systems for those customers who wants to focus on their business instead of wasting time to automate it.</p>
  </section>

  <aside class="newsletter">
    <h3>NEWESLETTER</h3>
    <div class="email">Your Email</div>
    <div class="go">GO</div>
    <div class="note">Subscribe to update latest news</div>
  </aside>

  <div class="partners">
    <div class="badge sky" style="left:8px;width:61px"></div>
    <div class="badge slate" style="left:78px;width:89px"></div>
    <div class="badge pale" style="left:182px;width:96px"></div>
    <div class="badge night" style="left:290px;width:163px"></div>
    <div class="badge sky" style="left:463px;width:61px"></div>
    <div class="badge slate" style="left:534px;width:88px"></div>
    <div class="badge pale" style="left:638px;width:96px"></div>
    <div class="badge night" style="left:744px;width:164px"></div>
  </div>

  <footer class="site-footer">
    <span style="left:132px">FOLLOW US</span>
    <i class="social-dot" style="left:242px"></i>
    <span style="left:266px">Friendlane</span>
    <i class="social-dot" style="left:347px"></i>
    <span style="left:370px">@Chirpwell</span>
    <span style="left:815px;font-size:11px">Copyright HCDS All Right Reserved 2013-14.</span>
  </footer>
  <div class="footer-base"></div>
</body>
</html>
```